Business Cards for Logistics Company

Looking to update Business Card Design.
Logo is attached. Blue background is not a part of the logo, you can remove it in layers.

Company: Harbor Crest Freightways
Industry: Logistics, Container Shipping

Address:
418 Willow Bend Ave
Marlow Point OR 97419

Phones:
p. 503-555-0143
f. 503-555-0178
c. very by person's name

Website: www.hcfroute.example

Design has to include person's name and position.
OLD Design is included.

B2B

Business

Card Size (non standard): 1039 x 697 pixels, 300dpi
Template is attached.

Font styles to use
Serif
Sans Serif

```html
<!DOCTYPE html>
<html lang="en">
<head>
<meta charset="utf-8">
<title>Harbor Crest Freightways – Business Cards</title>
<link rel="stylesheet" href="https://fonts.googleapis.com/css2?family=Open+Sans:wght@400;600&display=swap">
<style>
  :root {
    --backdrop: #4a423d;
    --card: #0b0b0c;
    --card-edge: #1c1c1e;
    --accent: #1e8fd6;
    --ink: #f2f2f2;
    --rule: #2a2a2d;
  }
  * { box-sizing: border-box; margin: 0; padding: 0; }
  html, body { width: 1200px; height: 900px; overflow: hidden; }
  body {
    background: var(--backdrop);
    font-family: "Open Sans", Arial, sans-serif;
    position: relative;
  }
  .card {
    position: absolute;
    width: 520px;
    height: 349px;
    background: var(--card);
    border: 1px solid var(--card-edge);
    box-shadow: 0 10px 30px rgba(0,0,0,.45);
  }
  .card--front { left: 45px; top: 276px; }
  .card--back { left: 635px; top: 276px; }

  /* front */
  .front-brand {
    position: absolute;
    left: 30px; top: 128px;
    width: 232px;
    display: flex; align-items: center; gap: 12px;
  }
  .brand-square {
    width: 34px; height: 34px; flex: none;
    background: var(--accent);
  }
  .brand-name {
    font-weight: 600;
    font-size: 19px;
    line-height: 1.2;
    color: var(--accent);
  }
  .front-divider {
    position: absolute;
    left: 278px; top: 60px;
    width: 1px; height: 230px;
    background: var(--rule);
  }
  .contact {
    position: absolute;
    left: 300px; top: 58px;
    width: 205px;
    color: var(--ink);
    font-size: 14px;
    line-height: 1.4;
  }
  .contact__name { color: var(--accent); font-weight: 600; font-size: 17px; }
  .contact__role { font-size: 13px; margin-bottom: 22px; }
  .contact__address { margin-bottom: 20px; }
  .contact__line { display: flex; align-items: center; gap: 9px; }
  .contact__line svg { width: 11px; height: 11px; fill: var(--accent); flex: none; }

  /* back */
  .back-brand {
    position: absolute;
    left: 0; right: 0; top: 70px;
    display: flex; justify-content: center; align-items: center; gap: 14px;
  }
  .back-brand .brand-name { font-size: 22px; }
  .back-copy {
    position: absolute;
    left: 0; right: 0; top: 175px;
    text-align: center;
    color: var(--ink);
    font-size: 13px;
    line-height: 1.55;
  }
  .back-copy__tagline { color: var(--accent); font-size: 15px; font-weight: 600; margin-bottom: 4px; }
  .back-copy__web { color: var(--accent); font-weight: 600; margin-top: 4px; }
</style>
</head>
<body>

<section class="card card--front" aria-label="Business card front">
  <div class="front-brand">
    <span class="brand-square"></span>
    <span class="brand-name">Harbor Crest Freightways</span>
  </div>
  <div class="front-divider"></div>
  <div class="contact">
    <div class="contact__name">Dmitri Valenko</div>
    <div class="contact__role">General Manager</div>
    <div class="contact__address">418 Willow Bend Ave<br>Marlow Point OR 97419</div>
    <div class="contact__line">
      <svg viewBox="0 0 12 12" aria-hidden="true"><path d="M2.5 1l2 2.2-1 1.3a7 7 0 0 0 4 4l1.3-1 2.2 2-1.3 1.5C5 10.5 1.5 7 1 2.3z"/></svg>
      <span>503-555-0143</span>
    </div>
    <div class="contact__line">
      <svg viewBox="0 0 12 12" aria-hidden="true"><path d="M3 1h5v3H3zM1 5h10v6H1zm2 2v1h2V7zm4 0v1h2V7z"/></svg>
      <span>503-555-0178</span>
    </div>
    <div class="contact__line">
      <svg viewBox="0 0 12 12" aria-hidden="true"><path d="M3.5 0h5a1 1 0 0 1 1 1v10a1 1 0 0 1-1 1h-5a1 1 0 0 1-1-1V1a1 1 0 0 1 1-1zm.5 1.5v7.5h4V1.5z"/></svg>
      <span>971.555.0192</span>
    </div>
    <div class="contact__line">
      <svg viewBox="0 0 12 12" aria-hidden="true"><path d="M0 2.5h12v7H0zm1 .8v.4l5 3.2 5-3.2v-.4z"/></svg>
      <span>info@hcfroute.example</span>
    </div>
  </div>
</section>

<section class="card card--back" aria-label="Business card back">
  <div class="back-brand">
    <span class="brand-square"></span>
    <span class="brand-name">Harbor Crest Freightways</span>
  </div>
  <div class="back-copy">
    <div class="back-copy__tagline">International Transportation Solutions</div>
    <div>Ocean &amp; Air Freight &nbsp;|&nbsp; Loading &amp; Storage</div>
    <div>Multimodal Transport</div>
    <div class="back-copy__web">www.hcfroute.example</div>
  </div>
</section>

</body>
</html>
```